Etikett für einen Rosé Wein
Zielgruppe
Wir sind ein Weingut und benötigen ein neues Etikett für unseren Muskattrollinger Rosé. Unsere Kunden sind eher traditionelle Weinkäufer.
Aufgabenstellung
Format:
Höhe: 9 cm
Breite: 11 cm
Da es nur ein Vorderetikett gibt, müssen alle relevanten Angaben (Hersteller, Alkohol, Inhalt in L, Rebsorte, etc.) enthalten sein. (siehe Flaschenabbildung anbei)
WÜRTTEMBERG
2019er
Muskattrollinger Rosé
DEUTSCHER QUALITÄTSWEIN
11,0 % Vol.
0,75 l
Enthält Sulfite
A.P.Nr. 58271346
Abfüller
Straße / PLZ / Ort / Tel.
Der Flaschenverschluss ist schwarz d.h. das neue Etikettendesign sollte dazu passen.
Bisher ist der Hintergrund des Weinetiketts schwarz. Dies muss jedoch nicht so bleiben.
Im Anhang finden Sie außerdem ein Plakat. Ggf. können Sie für das Flaschendesign einige nostalgische Elemente davon übernehmen.

```html
<!DOCTYPE html>
<html lang="de">
<head>
<meta charset="utf-8">
<title>Muskattrollinger Rosé – Etikett</title>
<link rel="stylesheet" href="https://fonts.googleapis.com/css2?family=Allura&family=Barlow:wght@400;500&family=Barlow+Condensed:wght@400;500&display=swap">
<style>
  :root {
    --backdrop: #ececec;
    --label-black: #050505;
    --gold: #c9a35a;
    --gold-light: #e8cf94;
    --gold-dark: #9c7634;
    --leaf-orange: #d8894c;
    --leaf-taupe: #9e8570;
    --white: #ffffff;
    --fine-print: #e6e6e6;
  }
  * { box-sizing: border-box; margin: 0; padding: 0; }
  html, body {
    width: 1200px; height: 983px; overflow: hidden;
    background: var(--backdrop);
  }
  .wine-label {
    position: absolute; left: 160px; top: 131px;
    width: 880px; height: 720px;
    background: var(--label-black);
    overflow: hidden;
    font-family: "Barlow", Arial, sans-serif;
    color: var(--white);
  }
  .leaf-art { position: absolute; inset: 0; width: 100%; height: 100%; }
  .gold-frame {
    position: absolute; left: 23px; right: 23px; top: 30px; bottom: 30px;
    border: 3px solid var(--gold);
  }
  .heading { position: absolute; left: 0; right: 0; text-align: center; }
  .region {
    top: 170px;
    font-family: "Allura", cursive;
    font-size: 112px; line-height: 1;
    color: var(--gold);
    letter-spacing: 2px;
  }
  .vintage {
    top: 282px; font-size: 44px; font-weight: 400; color: var(--gold-light);
  }
  .variety {
    top: 330px; font-size: 50px; font-weight: 500; color: var(--white);
  }
  .divider {
    position: absolute; left: 225px; width: 430px; top: 406px;
    height: 3px; background: var(--gold);
  }
  .quality-class {
    top: 428px; font-size: 29px; letter-spacing: 1px; color: var(--white);
  }
  .quality-seal { position: absolute; left: 545px; top: 434px; width: 284px; height: 284px; }
  .fine-print {
    position: absolute; font-size: 16px; line-height: 1.3; color: var(--fine-print);
  }
  .fine-print--left { left: 38px; top: 624px; }
  .fine-print--center { left: 311px; width: 200px; top: 624px; text-align: center; }
</style>
</head>
<body>
  <div class="wine-label">
    <svg class="leaf-art" viewBox="0 0 880 720" role="img" aria-label="Illustrierte Weinlaub-Blätter in Orange und Taupe an den Rändern des Etiketts">
      <defs>
        <linearGradient id="leafLeft" x1="0" y1="0" x2="0" y2="1">
          <stop offset="0" stop-color="var(--leaf-orange)"/>
          <stop offset="0.5" stop-color="var(--leaf-taupe)"/>
          <stop offset="1" stop-color="var(--leaf-orange)"/>
        </linearGradient>
        <linearGradient id="leafRight" x1="0" y1="0" x2="0" y2="1">
          <stop offset="0" stop-color="var(--leaf-taupe)"/>
          <stop offset="0.5" stop-color="var(--leaf-orange)"/>
          <stop offset="1" stop-color="var(--leaf-taupe)"/>
        </linearGradient>
      </defs>
      <path fill="url(#leafLeft)" d="M0 0 H260 C230 40 180 60 170 110 C150 150 190 190 150 240 C120 280 160 330 130 380 C100 430 170 470 150 530 C130 580 110 620 70 660 L0 700 Z"/>
      <path fill="url(#leafRight)" d="M880 0 V720 H820 C760 680 800 620 770 570 C740 520 800 470 760 420 C730 370 790 330 780 270 C770 210 720 170 760 110 C780 70 800 40 790 0 Z"/>
    </svg>
    <svg class="leaf-art" viewBox="0 0 880 720" aria-hidden="true">
      <circle cx="95" cy="705" r="160" fill="var(--leaf-orange)"/>
    </svg>

    <div class="gold-frame"></div>

    <div class="heading region">Württemberg</div>
    <div class="heading vintage">2019er</div>
    <div class="heading variety">Muskattrollinger Rosé</div>
    <div class="divider"></div>
    <div class="heading quality-class">DEUTSCHER QUALITÄTSWEIN</div>

    <svg class="quality-seal" viewBox="0 0 284 284" aria-hidden="true">
      <defs>
        <linearGradient id="sealGold" x1="0" y1="0" x2="1" y2="1">
          <stop offset="0" stop-color="var(--gold-light)"/>
          <stop offset="0.5" stop-color="var(--gold)"/>
          <stop offset="1" stop-color="var(--gold-dark)"/>
        </linearGradient>
      </defs>
      <circle cx="142" cy="142" r="138" fill="url(#sealGold)"/>
      <circle cx="142" cy="142" r="104" fill="none" stroke="var(--gold-dark)" stroke-width="3"/>
    </svg>

    <div class="fine-print fine-print--left">11,0 % Vol.<br>0,75 l<br>Enthält Sulfite</div>
    <div class="fine-print fine-print--center">A.P.Nr. 58271346<br>Abfüller<br>Straße / PLZ / Ort / Tel.</div>
  </div>
</body>
</html>
```